Manufacturing company needs new business card.

I need a unique Business Card that will truly stand out. Nothing too busy. Simple is good, right? Not looking for a standard design either. No cookie cutter layout. I am just looking for something interesting and a bit different. Does't have to completely off the wall crazy, just not your run of the mill business card. Clean and modern with a touch of industrial.

Target Market(s)

Air conditioning industry, Architects, builders.

Industry/Entity Type

Business

Contact Information for Business Card

Details to be included on card are:

Peter Vance
Managing Director

T: 1300 847 519
M: 0428 593 174
W: www.brenvaleworks.com.au
E: peter.vance@brenvaleworks.com.au
A: 58 Harwick Lane, Sydney NSW 2000

Font styles to use
Sans Serif

Colors
0355a3
848484
fbfbfb

Requirements
Must have
• Card design must be landscape.

```html
<!DOCTYPE html>
<html lang="en">
<head>
<meta charset="utf-8">
<title>Brenvale Works – Business Card</title>
<link rel="stylesheet" href="https://fonts.googleapis.com/css2?family=Source+Sans+3:wght@300;400;600;700&display=swap">
<style>
  :root {
    --brand-blue: #0355a3;
    --card-blue: #1f4fb0;
    --name-blue: #2a5cc0;
    --steel-grey: #848484;
    --charcoal: #222222;
    --paper: #fbfbfb;
    --muted-text: #d8d8d8;
    --stage-top: #c9c9c9;
    --stage-bottom: #e9e9e9;
  }
  * { margin: 0; padding: 0; box-sizing: border-box; }
  html, body { width: 1200px; height: 900px; overflow: hidden; }
  body {
    position: relative;
    font-family: "Source Sans 3", sans-serif;
    background: linear-gradient(180deg, var(--stage-top) 0%, var(--stage-bottom) 70%, #e6e6e6 100%);
  }
  .card {
    position: absolute;
    top: 306px;
    width: 440px;
    height: 272px;
    border-radius: 8px;
    overflow: hidden;
  }
  .card--front { left: 149px; background: var(--charcoal); }
  .card--back { left: 608px; background: var(--card-blue); }

  /* front */
  .front-accent { position: absolute; left: 0; top: 34px; }
  .holder { position: absolute; left: 36px; top: 32px; }
  .holder__name { color: var(--name-blue); font-size: 18px; font-weight: 600; line-height: 20px; }
  .holder__title { color: var(--paper); font-size: 12.5px; font-weight: 400; line-height: 16px; }

  .brand {
    position: absolute;
    display: flex;
    align-items: center;
    gap: 18px;
  }
  .brand__mark { width: 44px; height: 44px; }
  .brand__name { font-size: 26px; font-weight: 600; letter-spacing: 0.2px; white-space: nowrap; }
  .card--front .brand { right: 28px; top: 96px; }
  .card--front .brand__mark { background: var(--name-blue); }
  .card--front .brand__name { color: var(--name-blue); }

  .contacts { position: absolute; left: 24px; top: 170px; list-style: none; }
  .contacts li {
    display: flex; align-items: center; gap: 6px;
    height: 16px; color: var(--muted-text); font-size: 12.5px; font-weight: 400;
  }
  .contacts svg { width: 10px; height: 10px; flex: none; }
  .address {
    position: absolute; left: 312px; top: 202px;
    color: var(--muted-text); font-size: 12.5px; line-height: 16px; font-style: normal;
  }
  .front-band { position: absolute; left: 0; bottom: 0; }

  /* back */
  .back-field {
    position: absolute; inset: 0;
    background: linear-gradient(180deg, #1e4db0 0%, #2152b6 100%);
  }
  .card--back .brand { left: 68px; top: 114px; }
  .card--back .brand__mark { background: var(--paper); }
  .card--back .brand__name { color: var(--paper); }
  .back-web {
    position: absolute; left: 129px; top: 219px;
    color: var(--paper); font-size: 12.5px; font-weight: 700;
  }
</style>
</head>
<body>
  <section class="card card--front" aria-label="Business card front">
    <svg class="front-accent" width="26" height="32" viewBox="0 0 26 32" aria-hidden="true">
      <polygon points="0,0 7,0 11,32 0,32" fill="var(--name-blue)"/>
      <polygon points="9,0 24,0 24,32 13,32" fill="var(--steel-grey)"/>
    </svg>

    <div class="holder">
      <p class="holder__name">Peter Vance</p>
      <p class="holder__title">Managing Director</p>
    </div>

    <div class="brand">
      <span class="brand__mark"></span>
      <span class="brand__name">Brenvale Works</span>
    </div>

    <ul class="contacts">
      <li>
        <svg viewBox="0 0 10 10" aria-hidden="true"><path d="M2 1 L4 3 L3 4 Q4.5 6 6 7 L7 6 L9 8 L8 9.5 Q3 8.5 0.5 2 Z" fill="var(--name-blue)"/></svg>
        1300 847 519
      </li>
      <li>
        <svg viewBox="0 0 10 10" aria-hidden="true"><rect x="2.5" y="0.5" width="5" height="9" rx="1" fill="none" stroke="var(--name-blue)" stroke-width="1.2"/></svg>
        0428 593 174
      </li>
      <li>
        <svg viewBox="0 0 10 10" aria-hidden="true"><circle cx="5" cy="5" r="4.5" fill="var(--name-blue)"/><path d="M0.5 5 H9.5 M5 0.5 Q2 5 5 9.5 M5 0.5 Q8 5 5 9.5" stroke="var(--charcoal)" stroke-width="0.8" fill="none"/></svg>
        www.brenvaleworks.com.au
      </li>
      <li>
        <svg viewBox="0 0 10 10" aria-hidden="true"><rect x="0.5" y="2" width="9" height="6.5" fill="var(--name-blue)"/><path d="M0.5 2 L5 5.5 L9.5 2" stroke="var(--charcoal)" stroke-width="0.9" fill="none"/></svg>
        peter.vance@brenvaleworks.com.au
      </li>
    </ul>

    <address class="address">58 Harwick Lane,<br>Sydney NSW 2000</address>

    <svg class="front-band" width="440" height="20" viewBox="0 0 440 20" aria-hidden="true">
      <polygon points="0,6 260,6 250,20 0,20" fill="var(--name-blue)"/>
      <polygon points="264,2 440,2 440,20 248,20" fill="var(--steel-grey)"/>
    </svg>
  </section>

  <section class="card card--back" aria-label="Business card back">
    <div class="back-field" role="img" aria-label="Repeating brand pattern in deep blue tones"></div>
    <div class="brand">
      <span class="brand__mark"></span>
      <span class="brand__name">Brenvale Works</span>
    </div>
    <p class="back-web">www.brenvaleworks.com.au</p>
  </section>
</body>
</html>
```